Quillory Nest Business Card

I need a business card design. We are a collaborate online training company. Our colors are gray and green. Our website is QuilloryNest.com

I would like an area for a profile picture within the card

```html
<!DOCTYPE html>
<html lang="en">
<head>
<meta charset="utf-8">
<title>Quillory Nest Business Card</title>
<link href="https://fonts.googleapis.com/css2?family=Roboto+Condensed:wght@700&family=Roboto:wght@400&display=swap" rel="stylesheet">
<style>
  :root {
    --canvas: #e9e9e6;
    --paper: #ffffff;
    --paper-shade: #f1f1f1;
    --green: #8cc63f;
    --green-deep: #6fa52d;
    --green-light: #cfe88f;
    --dark: #1f2a2c;
    --charcoal: #2f3c3f;
    --ink: #1b1b1b;
    --muted: #555b5c;
  }
  * { box-sizing: border-box; margin: 0; padding: 0; }
  html, body { width: 1200px; height: 1023px; overflow: hidden; }
  body { background: var(--canvas); position: relative; font-family: "Roboto", Arial, sans-serif; }

  .card {
    position: absolute;
    width: 540px;
    height: 310px;
    border-radius: 16px;
    overflow: hidden;
    box-shadow: 0 10px 28px rgba(0,0,0,0.18);
  }

  /* Front */
  .card--front {
    left: 70px; top: 110px;
    background: linear-gradient(160deg, var(--paper) 55%, var(--paper-shade));
  }
  .front__corner-block {
    position: absolute; left: 0; top: 0;
    width: 170px; height: 112px;
    background: var(--green);
  }
  .front__panel {
    position: absolute; left: 130px; top: 186px;
    width: 200px; height: 124px;
    background: linear-gradient(135deg, var(--green-light), var(--green) 90%);
  }
  .brand {
    position: absolute;
    display: flex; align-items: center; gap: 10px;
    font-family: "Roboto Condensed", "Arial Narrow", sans-serif;
    font-weight: 700;
    letter-spacing: -0.5px;
    white-space: nowrap;
    line-height: 1;
  }
  .brand__dot { border-radius: 50%; background: var(--green); flex: none; }
  .brand--front { left: 22px; top: 128px; font-size: 40px; color: var(--ink); }
  .brand--front .brand__dot { width: 30px; height: 30px; }

  .profile {
    position: absolute; right: 54px; top: 20px;
    width: 96px; height: 96px; border-radius: 50%;
    border: 2px solid var(--green);
    padding: 4px;
  }
  .profile__photo {
    width: 100%; height: 100%; border-radius: 50%;
    background: linear-gradient(160deg, #e7e7e7, #9ca2a4);
  }
  .profile__name {
    position: absolute; right: 22px; top: 122px;
    font-size: 13px; color: var(--muted);
  }
  .contact {
    position: absolute; right: 18px; top: 190px;
    list-style: none;
    display: flex; flex-direction: column; gap: 9px; align-items: flex-end;
  }
  .contact__item {
    display: flex; align-items: center; gap: 8px;
    font-size: 12.5px; color: var(--ink);
    white-space: nowrap;
  }
  .contact__icon { width: 16px; height: 16px; flex: none; }

  /* Back */
  .card--back {
    left: 610px; top: 580px;
    background: radial-gradient(ellipse at 65% 40%, var(--charcoal), var(--dark) 80%);
  }
  .back__stripe {
    position: absolute; left: 0; right: 0; top: 228px; height: 32px;
    background: var(--green);
    display: flex; align-items: center; justify-content: center;
    border-top: 6px solid var(--green-deep);
  }
  .back__web { font-size: 13px; color: #ffffff; letter-spacing: 0.3px; }
  .brand--back { left: 50%; top: 94px; transform: translateX(-50%); font-size: 56px; color: #ffffff; }
  .brand--back .brand__dot { width: 42px; height: 42px; }
</style>
</head>
<body>

<section class="card card--front" aria-label="Business card front">
  <div class="front__corner-block"></div>
  <div class="front__panel"></div>
  <div class="brand brand--front"><span class="brand__dot"></span>Quillory Nest</div>

  <div class="profile">
    <div class="profile__photo" role="img" aria-label="Profile picture area"></div>
  </div>
  <p class="profile__name">Your name</p>

  <ul class="contact">
    <li class="contact__item">88- 456-70912
      <svg class="contact__icon" viewBox="0 0 16 16" aria-hidden="true">
        <circle cx="8" cy="8" r="7" fill="none" stroke="#8cc63f" stroke-width="1.2"/>
        <path d="M5.5 4.5l1.5 0 .6 2-1 .8a5 5 0 0 0 2.1 2.1l.8-1 2 .6 0 1.5c-3.6.4-6.4-2.4-6-6z" fill="#8cc63f"/>
      </svg>
    </li>
    <li class="contact__item">info@quillorynest.com
      <svg class="contact__icon" viewBox="0 0 16 16" aria-hidden="true">
        <rect x="2" y="4" width="12" height="8" fill="none" stroke="#8cc63f" stroke-width="1.2"/>
        <path d="M2 4l6 5 6-5" fill="none" stroke="#8cc63f" stroke-width="1.2"/>
      </svg>
    </li>
    <li class="contact__item">www.quillorynest.com
      <svg class="contact__icon" viewBox="0 0 16 16" aria-hidden="true">
        <circle cx="8" cy="8" r="6.5" fill="none" stroke="#8cc63f" stroke-width="1.2"/>
        <ellipse cx="8" cy="8" rx="3" ry="6.5" fill="none" stroke="#8cc63f" stroke-width="1"/>
        <path d="M1.5 8h13M2.5 5h11M2.5 11h11" stroke="#8cc63f" stroke-width="1"/>
      </svg>
    </li>
  </ul>
</section>

<section class="card card--back" aria-label="Business card back">
  <div class="brand brand--back"><span class="brand__dot"></span>Quillory Nest</div>
  <div class="back__stripe"><span class="back__web">www.quillorynest.com</span></div>
</section>

</body>
</html>
```